Snow & Ice Melter

We need a bag design for a new product our company is producing. Our company, Kestrel Winter Goods manufactures ice melt for melting snow. We are in the process of developing a new ice melt product called "Blizzard's Bane snow & ice melter". We would like to see designs that include a logo for the product, a snowman (that depicts Blizzard) and a wintery background. To get an idea of our current product packaging go to our website at http://www.kestrelwg.example

```html
<!DOCTYPE html>
<html lang="en">
<head>
<meta charset="utf-8">
<title>Blizzard's Bane Snow &amp; Ice Melter – Bag Front</title>
<link rel="stylesheet" href="https://fonts.googleapis.com/css2?family=Anton&family=Oswald:wght@500;700&display=swap">
<style>
  :root {
    --night-deep: #0f1a4a;
    --night-mid: #26368a;
    --night-light: #4a5fb4;
    --frost-white: #f4f7ff;
    --ice-blue: #b9c8f2;
    --title-shadow: #0a1236;
    --melt-yellow: #ffe12a;
    --melt-orange: #f7781c;
    --melt-red: #d8261c;
    --claim-yellow: #ffe93a;
    --ink-navy: #1b2c82;
    --art-light: #e9edf5;
    --art-shade: #aab4c8;
  }
  * { box-sizing: border-box; margin: 0; padding: 0; }
  html, body { width: 1075px; height: 1200px; overflow: hidden; }
  body { background: var(--frost-white); font-family: 'Oswald', sans-serif; }

  .bag-front {
    position: relative;
    width: 1075px;
    height: 1200px;
    overflow: hidden;
    background: linear-gradient(180deg,
      var(--night-deep) 0%,
      var(--night-mid) 38%,
      var(--night-light) 66%,
      var(--ice-blue) 84%,
      var(--frost-white) 93%);
  }

  .product-title {
    position: absolute;
    top: 70px;
    left: 0;
    width: 100%;
    text-align: center;
    font-family: 'Anton', sans-serif;
    font-weight: 400;
    font-size: 190px;
    line-height: 0.98;
    letter-spacing: 4px;
    color: var(--frost-white);
    text-shadow: 0 6px 0 var(--title-shadow), 0 0 18px rgba(185, 200, 242, 0.6);
    text-transform: uppercase;
  }

  .product-type {
    position: absolute;
    top: 448px;
    left: 0;
    width: 100%;
    text-align: center;
    font-family: 'Anton', sans-serif;
    font-size: 74px;
    letter-spacing: 2px;
    text-transform: uppercase;
    background: linear-gradient(180deg, var(--melt-yellow) 15%, var(--melt-orange) 55%, var(--melt-red) 90%);
    -webkit-background-clip: text;
    background-clip: text;
    color: transparent;
    filter: drop-shadow(0 3px 0 var(--title-shadow));
  }

  .claims {
    position: absolute;
    top: 590px;
    left: 100px;
    width: 430px;
    list-style: none;
    color: var(--claim-yellow);
    font-family: 'Oswald', sans-serif;
    font-weight: 700;
    text-transform: uppercase;
    text-shadow: 0 2px 4px rgba(10, 18, 54, 0.5);
  }
  .claims li { margin-bottom: 34px; line-height: 0.95; }
  .claim-lead { display: block; font-size: 92px; }
  .claim-sub { display: block; font-size: 52px; }
  .claim-small .claim-sub { font-size: 44px; }

  .mascot-art {
    position: absolute;
    left: 560px;
    top: 580px;
    width: 460px;
    height: 440px;
    border-radius: 28px;
    background: radial-gradient(ellipse at 50% 55%, var(--art-light) 0%, var(--art-light) 50%, var(--art-shade) 100%);
  }

  .net-weight {
    position: absolute;
    left: 90px;
    top: 1080px;
    color: var(--ink-navy);
    font-family: 'Oswald', sans-serif;
    font-weight: 700;
    font-size: 46px;
    line-height: 1.15;
  }

  .maker-mark {
    position: absolute;
    left: 600px;
    top: 1050px;
    display: flex;
    align-items: center;
    gap: 12px;
    color: var(--ink-navy);
    font-family: 'Oswald', sans-serif;
    font-weight: 700;
    font-size: 32px;
  }
  .maker-mark-square {
    width: 26px;
    height: 26px;
    background: var(--ink-navy);
  }
</style>
</head>
<body>
  <main class="bag-front">
    <h1 class="product-title">Blizzard's<br>Bane</h1>
    <p class="product-type">Snow &amp; Ice Melter</p>

    <ul class="claims">
      <li><span class="claim-lead">Superior</span><span class="claim-sub">Melting Power</span></li>
      <li><span class="claim-lead">Effective</span><span class="claim-sub">On Contact</span></li>
      <li class="claim-small"><span class="claim-sub">Environmentally</span><span class="claim-sub">Responsible</span></li>
    </ul>

    <div class="mascot-art" role="img" aria-label="Space for the Blizzard snowman mascot illustration"></div>

    <p class="net-weight">Net Wt. 50lb.<br>(9.1kg)</p>

    <div class="maker-mark">
      <span class="maker-mark-square"></span>
      <span>Kestrel Winter Goods</span>
    </div>
  </main>
</body>
</html>
```